One business card required with 2 company logos and 2 people's details

One business card required.
No preference on design - One side could show the 2 different business logos for the companies we own. The reverse could have the details shown below.
Another option could be one business one side and one business on the reverse. Happy to receive designs.

Karen Wibberley
07700 913 258
Joanna Pettifer
07700 927 341

website: truelymarvellous.example
email: info@truelymarvellous.example

website: ironheronoccasions.example
email: info:ironheronoccasions.example

May be nice to have icons instead of the words email/website?

I have included different versions of the logos to help with your design.

Contact Information for Business Card

see project overview

Requirements
Must have
• both company logos, both contact names and contact details

```html
<!DOCTYPE html>
<html lang="en">
<head>
<meta charset="utf-8">
<title>Business Cards</title>
<link rel="stylesheet" href="https://fonts.googleapis.com/css2?family=Poppins:wght@400;600&display=swap">
<style>
  :root {
    --page-bg: #2b2b2d;
    --card-black: #050506;
    --card-teal-top: #0f2c33;
    --card-teal-glow: #1d5660;
    --card-teal-bottom: #0a1a20;
    --brand-blue: #3f8ff0;
    --accent-cyan: #35b8ee;
    --name-cyan: #4cc6f5;
    --script-white: #f2f6f8;
    --feather-teal: #3aa7b3;
    --feather-violet: #7a6ad8;
  }
  * { box-sizing: border-box; margin: 0; padding: 0; }
  html, body { width: 1200px; height: 1108px; overflow: hidden; }
  body {
    background: var(--page-bg);
    font-family: "Poppins", sans-serif;
    position: relative;
  }
  .card {
    position: absolute;
    top: 194px;
    width: 420px;
    height: 720px;
    border-radius: 18px;
    overflow: hidden;
    display: flex;
    flex-direction: column;
    align-items: center;
  }
  .card--heron { left: 150px; background: var(--card-black); }
  .card--marvellous {
    left: 630px;
    background:
      radial-gradient(ellipse 70% 45% at 50% 42%, var(--card-teal-glow) 0%, transparent 70%),
      linear-gradient(180deg, var(--card-teal-top) 0%, var(--card-teal-bottom) 100%);
  }
  .brand {
    height: 420px;
    width: 100%;
    display: flex;
    align-items: center;
    justify-content: center;
    position: relative;
  }
  .brand-name {
    font-weight: 600;
    text-align: center;
    line-height: 1.15;
    position: relative;
    z-index: 1;
  }
  .card--heron .brand-name {
    color: var(--brand-blue);
    font-size: 40px;
    letter-spacing: 2px;
  }
  .card--marvellous .brand-name {
    color: var(--script-white);
    font-size: 42px;
  }
  .feather-art {
    position: absolute;
    top: 70px;
    left: 90px;
    width: 280px;
    height: 150px;
    border-radius: 50%;
    background: radial-gradient(ellipse at 40% 50%, var(--feather-teal) 0%, var(--feather-violet) 55%, transparent 75%);
    opacity: 0.55;
  }
  .contact {
    display: flex;
    flex-direction: column;
    align-items: center;
    color: var(--accent-cyan);
  }
  .divider {
    display: flex;
    align-items: center;
    gap: 10px;
    margin-bottom: 10px;
  }
  .divider-line { width: 34px; height: 2px; background: var(--accent-cyan); }
  .divider-icon { width: 24px; height: 24px; }
  .web-line { font-size: 17px; line-height: 1.5; }
  .person { margin-top: 14px; text-align: center; }
  .person-name { font-size: 20px; font-weight: 600; color: var(--name-cyan); line-height: 1.3; }
  .person-phone {
    font-size: 17px;
    line-height: 1.4;
    display: flex;
    align-items: center;
    justify-content: center;
    gap: 6px;
  }
  .phone-icon { width: 14px; height: 14px; }
</style>
</head>
<body>

<section class="card card--heron">
  <div class="brand">
    <p class="brand-name">IRON HERON<br>OCCASIONS</p>
  </div>
  <div class="contact">
    <div class="divider">
      <span class="divider-line"></span>
      <svg class="divider-icon" viewBox="0 0 24 24" fill="none" stroke="var(--accent-cyan)" stroke-width="1.5"><circle cx="12" cy="12" r="11"/><circle cx="12" cy="12" r="6"/><path d="M6 12h12M12 6c-2 2-2 10 0 12M12 6c2 2 2 10 0 12"/></svg>
      <svg class="divider-icon" viewBox="0 0 24 24" fill="none" stroke="var(--accent-cyan)" stroke-width="1.5"><circle cx="12" cy="12" r="11"/><rect x="6.5" y="8" width="11" height="8"/><path d="M6.5 8l5.5 4.5 5.5-4.5"/></svg>
      <span class="divider-line"></span>
    </div>
    <p class="web-line">ironheronoccasions.example</p>
    <p class="web-line">info@ironheronoccasions.example</p>
    <div class="person">
      <p class="person-name">Karen Wibberley</p>
      <p class="person-phone"><svg class="phone-icon" viewBox="0 0 24 24" fill="var(--accent-cyan)"><path d="M6.6 10.8a15 15 0 0 0 6.6 6.6l2.2-2.2a1 1 0 0 1 1-.25 11 11 0 0 0 3.6.6 1 1 0 0 1 1 1V20a1 1 0 0 1-1 1A17 17 0 0 1 3 4a1 1 0 0 1 1-1h3.5a1 1 0 0 1 1 1 11 11 0 0 0 .6 3.6 1 1 0 0 1-.25 1z"/></svg>07700 913 258</p>
    </div>
    <div class="person">
      <p class="person-name">Joanna Pettifer</p>
      <p class="person-phone"><svg class="phone-icon" viewBox="0 0 24 24" fill="var(--accent-cyan)"><path d="M6.6 10.8a15 15 0 0 0 6.6 6.6l2.2-2.2a1 1 0 0 1 1-.25 11 11 0 0 0 3.6.6 1 1 0 0 1 1 1V20a1 1 0 0 1-1 1A17 17 0 0 1 3 4a1 1 0 0 1 1-1h3.5a1 1 0 0 1 1 1 11 11 0 0 0 .6 3.6 1 1 0 0 1-.25 1z"/></svg>07700 927 341</p>
    </div>
  </div>
</section>

<section class="card card--marvellous">
  <div class="brand">
    <div class="feather-art" role="img" aria-label="Glowing teal and violet feather illustration"></div>
    <p class="brand-name">Truely<br>Marvellous</p>
  </div>
  <div class="contact">
    <div class="divider">
      <span class="divider-line"></span>
      <svg class="divider-icon" viewBox="0 0 24 24" fill="none" stroke="var(--accent-cyan)" stroke-width="1.5"><circle cx="12" cy="12" r="11"/><circle cx="12" cy="12" r="6"/><path d="M6 12h12M12 6c-2 2-2 10 0 12M12 6c2 2 2 10 0 12"/></svg>
      <svg class="divider-icon" viewBox="0 0 24 24" fill="none" stroke="var(--accent-cyan)" stroke-width="1.5"><circle cx="12" cy="12" r="11"/><rect x="6.5" y="8" width="11" height="8"/><path d="M6.5 8l5.5 4.5 5.5-4.5"/></svg>
      <span class="divider-line"></span>
    </div>
    <p class="web-line">truelymarvellous.example</p>
    <p class="web-line">info@truelymarvellous.example</p>
    <div class="person">
      <p class="person-name">Karen Wibberley</p>
      <p class="person-phone"><svg class="phone-icon" viewBox="0 0 24 24" fill="var(--accent-cyan)"><path d="M6.6 10.8a15 15 0 0 0 6.6 6.6l2.2-2.2a1 1 0 0 1 1-.25 11 11 0 0 0 3.6.6 1 1 0 0 1 1 1V20a1 1 0 0 1-1 1A17 17 0 0 1 3 4a1 1 0 0 1 1-1h3.5a1 1 0 0 1 1 1 11 11 0 0 0 .6 3.6 1 1 0 0 1-.25 1z"/></svg>07700 913 258</p>
    </div>
    <div class="person">
      <p class="person-name">Joanna Pettifer</p>
      <p class="person-phone"><svg class="phone-icon" viewBox="0 0 24 24" fill="var(--accent-cyan)"><path d="M6.6 10.8a15 15 0 0 0 6.6 6.6l2.2-2.2a1 1 0 0 1 1-.25 11 11 0 0 0 3.6.6 1 1 0 0 1 1 1V20a1 1 0 0 1-1 1A17 17 0 0 1 3 4a1 1 0 0 1 1-1h3.5a1 1 0 0 1 1 1 11 11 0 0 0 .6 3.6 1 1 0 0 1-.25 1z"/></svg>07700 927 341</p>
    </div>
  </div>
</section>

</body>
</html>
```